High-End audio shop owner needs a business card

I need a personal Business Card for my Audio shop which exists since 1962. We offer high Quality brands, professional Attention and run our own repair-service-department. I look for a design which will be printed on high Quality paper and shall convey trust to the Client that we are very serious. Language is german.

```html
<!DOCTYPE html>
<html lang="de">
<head>
<meta charset="utf-8">
<title>Klanghaus Berger – Visitenkarte</title>
<link rel="stylesheet" href="https://fonts.googleapis.com/css2?family=Montserrat:wght@800&family=Lato:wght@400;700;900&display=swap">
<style>
  :root {
    --backdrop: #1d1e21;
    --card-dark: #222426;
    --card-light: #dcdcdc;
    --accent: #ee6a1f;
    --text-soft: #c9c9c9;
    --text-ink: #1b1b1b;
    --dots: #555555;
  }
  * { margin: 0; padding: 0; box-sizing: border-box; }
  html, body {
    width: 1200px; height: 800px; overflow: hidden;
    background: var(--backdrop);
  }
  .stage {
    width: 1200px; height: 800px;
    display: flex; align-items: center; justify-content: center; gap: 48px;
  }
  .card {
    width: 520px; height: 300px; border-radius: 22px;
    position: relative;
    box-shadow: 0 18px 40px rgba(0,0,0,.45);
  }
  .card--front { background: var(--card-dark); color: var(--text-soft); }
  .card--back { background: var(--card-light); color: var(--text-ink); }

  .brand {
    font-family: "Montserrat", sans-serif; font-weight: 800;
    text-transform: uppercase; letter-spacing: 1px; white-space: nowrap;
  }
  .card--front .brand {
    position: absolute; left: 48px; top: 60px;
    font-size: 34px; color: var(--accent);
  }
  .holder { position: absolute; left: 48px; top: 128px; font-family: "Lato", sans-serif; }
  .holder__name {
    font-weight: 900; font-size: 17px; color: var(--accent);
    letter-spacing: 1px; text-transform: uppercase;
  }
  .holder__role { font-size: 13px; color: var(--text-soft); margin-top: 2px; }

  .contact {
    position: absolute; left: 48px; top: 188px;
    font-family: "Lato", sans-serif; font-size: 13px; line-height: 22px;
    color: var(--text-soft);
  }
  .contact__row { display: flex; align-items: center; gap: 6px; white-space: nowrap; }
  .contact__sep { color: #777; margin: 0 6px; }
  .contact__icon { width: 12px; height: 12px; fill: var(--accent); }
  .contact__web { display: block; letter-spacing: 2px; }
  .contact__web em { font-style: normal; color: var(--accent); }

  .note-title {
    position: absolute; left: 48px; top: 36px;
    font-family: "Lato", sans-serif; font-size: 15px; letter-spacing: 4px;
  }
  .note-lines {
    position: absolute; left: 48px; right: 48px; top: 78px;
    list-style: none;
  }
  .note-lines li { height: 24px; border-bottom: 2px dotted var(--dots); }
  .card--back .brand {
    position: absolute; right: 40px; bottom: 26px;
    font-size: 22px; color: var(--text-ink);
  }
</style>
</head>
<body>
<main class="stage">
  <section class="card card--front" aria-label="Vorderseite">
    <div class="brand">Klanghaus Berger</div>
    <div class="holder">
      <div class="holder__name">Lukas Brandt</div>
      <div class="holder__role">Geschäftsführer</div>
    </div>
    <div class="contact">
      <div class="contact__row">Postfach 123, Lindenstraße 2, Hamburg</div>
      <div class="contact__row">
        <svg class="contact__icon" viewBox="0 0 24 24" aria-hidden="true"><path d="M6.6 10.8a15 15 0 0 0 6.6 6.6l2.2-2.2a1 1 0 0 1 1-.25 11.4 11.4 0 0 0 3.6.6 1 1 0 0 1 1 1V20a1 1 0 0 1-1 1A17 17 0 0 1 3 4a1 1 0 0 1 1-1h3.5a1 1 0 0 1 1 1c0 1.25.2 2.45.6 3.6a1 1 0 0 1-.25 1z"/></svg>
        <span>(040) 456 7890</span>
        <span class="contact__sep">|</span>
        <svg class="contact__icon" viewBox="0 0 24 24" aria-hidden="true"><path d="M2 5h20v14H2z M2 5l10 8 10-8" fill="var(--accent)" stroke="var(--card-dark)" stroke-width="2"/></svg>
        <span>info@klanghaus-berger.de</span>
      </div>
      <div class="contact__web">www.<em>klanghaus-berger</em>.de</div>
    </div>
  </section>

  <section class="card card--back" aria-label="Rückseite">
    <div class="note-title">NOTIZEN</div>
    <ul class="note-lines">
      <li></li><li></li><li></li><li></li><li></li><li></li>
    </ul>
    <div class="brand">Klanghaus Berger</div>
  </section>
</main>
</body>
</html>
```